Bref créative
Fun, professional business cards/advertisment for dog boarding kennel
Bright Meadow Dog Boarding
I need double sided standard sized Business Card [3.5" x 2"]
Papyrus (name) and cambria (other type)
Bright & Fun-filled
Renata & Gideon - Certified Dog Lovers
481 Palomar Lane
Yellowknife, NT
brightmeadow@pawmail.example
http://www.brightmeadowdogboarding.example
Daily, weekly, monthly dog boarding.
Multi-dog discounts
Doggie day camp and overnight boarding
Individualized care, affordable rates
Formally Furlough Pet Camp & Boarding
Call to schedule services today!
On the back of the business cards we would like it quite simple- just the logo with our website and phone number
We would like the front to be able to be used as an advertisement....like made into a magnet, so on the front we would like our name, logo and small bullet points as noted in the other comments.
We would like a fun, happy, but simple appearance. Please keep the fonts the same as in the logo.
fonts to use
AI file of our logo as requested

```html
<!DOCTYPE html>
<html lang="en">
<head>
<meta charset="utf-8">
<title>Bright Meadow Dog Boarding – Business Cards</title>
<link rel="stylesheet" href="https://fonts.googleapis.com/css2?family=Caladea:ital,wght@0,400;0,700;1,400&family=Macondo&display=swap">
<style>
  :root {
    --backdrop: #e6e6e4;
    --card: #ffffff;
    --card-shade: #eeeeee;
    --brand-red: #c8372d;
    --brand-blue: #2f6fa8;
    --ink: #333333;
    --ink-soft: #666666;
    --art-light: #dbe8f3;
    --art-mid: #9fc0dc;
  }
  * { box-sizing: border-box; margin: 0; padding: 0; }
  html, body {
    width: 1200px; height: 869px; overflow: hidden;
    background: var(--backdrop);
  }
  .canvas {
    position: relative; width: 1200px; height: 869px;
  }
  .card {
    position: absolute; top: 280px;
    width: 540px; height: 309px;
    border-radius: 14px;
    background: linear-gradient(180deg, var(--card) 0%, var(--card-shade) 100%);
    box-shadow: 0 6px 18px rgba(0,0,0,.18);
    overflow: hidden;
    font-family: "Caladea", serif;
    color: var(--ink);
  }
  .card--back { left: 40px; }
  .card--front { left: 620px; }

  .logo-art {
    position: absolute;
    border-radius: 120px 120px 10px 10px;
    background: linear-gradient(180deg, var(--art-light), var(--art-mid));
  }
  .card--back .logo-art { left: 205px; top: 22px; width: 130px; height: 92px; }
  .card--front .logo-art { right: 24px; bottom: 38px; width: 150px; height: 104px; }

  .brand { text-align: center; }
  .brand__name {
    font-family: "Caladea", serif; font-weight: 400;
    color: var(--brand-red); font-size: 32px; line-height: 1;
  }
  .brand__sub {
    font-family: "Macondo", cursive; color: var(--brand-red);
    font-size: 18px; line-height: 1.1;
  }
  .brand__former {
    font-size: 8.5px; color: var(--brand-blue); letter-spacing: .3px;
  }
  .card--back .brand { position: absolute; top: 122px; left: 0; right: 0; }

  .owners {
    position: absolute; top: 204px; left: 0; right: 0; text-align: center;
    font-size: 14px; color: var(--ink);
  }
  .owners__names {
    font-family: "Macondo", cursive; color: var(--brand-blue); font-size: 24px;
  }
  .owners__amp { color: var(--brand-red); font-family: "Macondo", cursive; font-size: 22px; }

  .website {
    position: absolute; left: 0; right: 0; bottom: 30px;
    text-align: center; font-size: 13px; letter-spacing: 1px; color: var(--ink);
  }
  .rule {
    position: absolute; left: 60px; right: 60px; bottom: 55px;
    border-top: 1px solid #cfcfcf;
  }

  .card--front .brand { position: absolute; top: 20px; left: 26px; text-align: left; }
  .card--front .brand__name { font-size: 30px; }

  .services {
    position: absolute; top: 108px; left: 28px; list-style: none;
    font-size: 12.5px; line-height: 20px;
  }
  .services li { display: flex; align-items: center; gap: 8px; }
  .services svg { flex: none; }

  .contact {
    position: absolute; left: 28px; top: 232px; font-size: 11.5px; line-height: 16px;
  }
  .card--front .website {
    left: auto; right: 24px; bottom: 12px; text-align: right;
    color: var(--brand-red); font-size: 12px;
  }
</style>
</head>
<body>
<main class="canvas">

  <section class="card card--back">
    <div class="logo-art" role="img" aria-label="Logo illustration: smiling dog resting in a dome shelter"></div>
    <div class="brand">
      <p class="brand__name">Bright Meadow</p>
      <p class="brand__sub">Dog Boarding</p>
      <p class="brand__former">Formally Furlough Pet Camp and Boarding</p>
    </div>
    <p class="owners">
      <span class="owners__names">Renata</span> <span class="owners__amp">&amp;</span>
      <span class="owners__names">Gideon</span> · Certified dog lovers
    </p>
    <div class="rule"></div>
    <p class="website">www.brightmeadowdogboarding.example</p>
  </section>

  <section class="card card--front">
    <div class="brand">
      <p class="brand__name">Bright Meadow</p>
      <p class="brand__sub">Dog Boarding</p>
      <p class="brand__former">Formally Furlough Pet Camp and Boarding</p>
    </div>
    <ul class="services">
      <li><svg width="11" height="11" viewBox="0 0 11 11"><circle cx="5.5" cy="5.5" r="5" fill="#2f6fa8"/><path d="M3 5.7 4.8 7.4 8 3.8" stroke="#fff" stroke-width="1.4" fill="none"/></svg>Daily, weekly, monthly dog boarding.</li>
      <li><svg width="11" height="11" viewBox="0 0 11 11"><circle cx="5.5" cy="5.5" r="5" fill="#2f6fa8"/><path d="M3 5.7 4.8 7.4 8 3.8" stroke="#fff" stroke-width="1.4" fill="none"/></svg>Multi-dog discounts</li>
      <li><svg width="11" height="11" viewBox="0 0 11 11"><circle cx="5.5" cy="5.5" r="5" fill="#2f6fa8"/><path d="M3 5.7 4.8 7.4 8 3.8" stroke="#fff" stroke-width="1.4" fill="none"/></svg>Doggie day camp and overnight boarding</li>
      <li><svg width="11" height="11" viewBox="0 0 11 11"><circle cx="5.5" cy="5.5" r="5" fill="#2f6fa8"/><path d="M3 5.7 4.8 7.4 8 3.8" stroke="#fff" stroke-width="1.4" fill="none"/></svg>Individualized care, affordable rates</li>
      <li><svg width="11" height="11" viewBox="0 0 11 11"><circle cx="5.5" cy="5.5" r="5" fill="#2f6fa8"/><path d="M3 5.7 4.8 7.4 8 3.8" stroke="#fff" stroke-width="1.4" fill="none"/></svg>Formally Furlough Pet Camp &amp; Boarding</li>
    </ul>
    <div class="contact">
      <p>Phone: 867-555-0142</p>
      <p>Email: brightmeadow@pawmail.example</p>
    </div>
    <div class="logo-art" role="img" aria-label="Illustration: smiling dog peeking out of a dome shelter"></div>
    <p class="website">www.brightmeadowdogboarding.example</p>
  </section>

</main>
</body>
</html>
```